Flyer Design for Private Car Service

Flyer should cater to Business Travelers and Executives who travel Business Class or First Class.
Flyer should include images attached.
Flyer should include the below text
Dallas to Austin
Chauffeured SUVs
• Travel Dallas to Austin in a new 2025 Marlow Strider for $499 one-way
• Trip includes a Uniformed Chauffeur who has a Commercial Drivers License (CDL)
• You can Schedule Chauffeur Pickup at Your Home in Dallas
• Our Chauffeur will Drop You Off at Your Final Destination in Austin
• You can Schedule Chauffeur Return Pickup in Austin and Return Back to Dallas.
• We offer Faster Times on Door-to-Door Travel than Bluecrest Airways
• We offer Comparable Prices on Door-to-Door Travel Times than Bluecrest Airways
• All of our trips are insured with $500k of commercial auto insurance
• Our Passengers can Talk on Cell Phone & Conduct Quill calls Throughout Travel
• Our Passengers have Maximum Privacy, Comfort and First-Class Amenities.
• Our Passengers Avoid Harwick Vale Field and KPR Airport hassles & delays
• Member Brenton Chamber of Commerce, Larkmoor Chamber of Commerce.
• Book your trip today at www.ridemarquel.example
Target Market(s)
Business Travelers
Look and feel
Each slider illustrates characteristics of the customer's brand and the style your logo design should communicate.

```html
<!DOCTYPE html>
<html lang="en">
<head>
<meta charset="utf-8">
<title>Dallas to Austin Chauffeured SUVs</title>
<link rel="stylesheet" href="https://fonts.googleapis.com/css2?family=Montserrat:wght@500;600;700;800&family=Playfair+Display:wght@500&display=swap">
<style>
  :root {
    --blush: #ecdcd8;
    --red: #e8262d;
    --ink: #0a0a0a;
    --white: #ffffff;
    --photo-light: #d9d3cf;
    --photo-mid: #8f8c8a;
    --photo-dark: #2a2a2a;
  }
  * { margin: 0; padding: 0; box-sizing: border-box; }
  html, body { width: 927px; height: 1200px; overflow: hidden; background: var(--ink); }
  .flyer {
    position: relative; width: 927px; height: 1200px; overflow: hidden;
    background: var(--ink); font-family: "Montserrat", sans-serif; color: var(--white);
  }
  .header-band { position: absolute; left: 0; top: 0; width: 927px; height: 210px; background: var(--blush); }
  .brand {
    position: absolute; left: 0; width: 927px; top: 102px; text-align: center;
    font-family: "Playfair Display", serif; font-weight: 500; font-size: 58px;
    letter-spacing: 2px; color: var(--ink);
  }
  .price-badge { position: absolute; left: 723px; top: 43px; width: 186px; height: 186px; }
  .hero-photo {
    position: absolute; left: 0; top: 210px; width: 927px; height: 495px;
    background: linear-gradient(180deg, #ece8e4 0%, #cfc9c4 40%, #6b6b6b 62%, #bdb6b0 80%, #d3ccc6 100%);
    border-top: 1px solid #333;
  }
  .book-pill {
    position: absolute; left: 158px; top: 210px; width: 611px; height: 111px;
    background: var(--red); border-radius: 56px; text-align: center; font-weight: 700;
  }
  .book-pill .line-one { margin-top: 18px; font-size: 35px; line-height: 40px; color: var(--white); }
  .book-pill .line-one b { color: var(--ink); font-weight: 700; }
  .book-pill .url { font-size: 35px; line-height: 42px; font-weight: 800; color: var(--ink); }
  .inset-photo { position: absolute; top: 545px; height: 218px; border: 1px solid #222; }
  .inset-photo.arrival {
    left: 132px; width: 326px;
    background: linear-gradient(160deg, #e7e4e0 0%, #9a9794 35%, var(--photo-dark) 70%, #1a1a1a 100%);
  }
  .inset-photo.team {
    left: 468px; width: 327px;
    background: linear-gradient(100deg, #f2f2f2 0%, #3a6fb0 25%, #bfbab5 45%, var(--photo-dark) 75%, #161616 100%);
  }
  .headline-pill {
    position: absolute; left: 180px; top: 750px; width: 567px; height: 93px;
    background: var(--red); border-radius: 47px; text-align: center; font-weight: 600;
  }
  .headline-pill h1 { font-size: 49px; line-height: 52px; margin-top: 8px; font-weight: 600; letter-spacing: 0.5px; }
  .headline-pill h2 { font-size: 29px; line-height: 30px; font-weight: 600; letter-spacing: 0.5px; }
  .features { position: absolute; left: 62px; top: 869px; list-style: none; }
  .features li {
    position: relative; padding-left: 48px; height: 25px;
    font-size: 16.5px; line-height: 25px; font-weight: 500; letter-spacing: 0.5px; white-space: nowrap;
  }
  .features li::before {
    content: ""; position: absolute; left: 2px; top: 6px; width: 22px; height: 12px;
    border: 2px solid var(--red); border-radius: 50%;
  }
</style>
</head>
<body>
<main class="flyer">
  <header class="header-band">
    <div class="brand">Marquel</div>
  </header>

  <div class="hero-photo" role="img" aria-label="Four uniformed chauffeurs standing beside black, white and red SUVs in front of a dealership building"></div>

  <svg class="price-badge" viewBox="0 0 186 186" aria-label="$499 one-way">
    <polygon fill="#0a0a0a" points="93,0 101,22 114,3 117,26 134,10 132,33 152,22 144,44 166,38 155,58 178,58 163,74 186,80 168,93 186,106 163,112 178,128 155,128 166,148 144,142 152,164 132,153 134,176 117,160 114,183 101,164 93,186 85,164 72,183 69,160 52,176 54,153 34,164 42,142 20,148 31,128 8,128 23,112 0,106 18,93 0,80 23,74 8,58 31,58 20,38 42,44 34,22 54,33 52,10 69,26 72,3 85,22"/>
    <text x="96" y="96" text-anchor="middle" fill="#e8262d" font-family="Montserrat, sans-serif" font-weight="800" font-size="50"><tspan font-size="24" dy="-20">$</tspan><tspan dy="20">499</tspan></text>
    <text x="93" y="126" text-anchor="middle" fill="#ffffff" font-family="Montserrat, sans-serif" font-weight="600" font-size="21">one-way</text>
  </svg>

  <div class="book-pill">
    <p class="line-one">Book your trip <b>today at</b></p>
    <p class="url">www.ridemarquel.example</p>
  </div>

  <div class="inset-photo arrival" role="img" aria-label="Chauffeur assisting a business traveler with luggage beside a black SUV"></div>
  <div class="inset-photo team" role="img" aria-label="Row of four uniformed chauffeurs in caps and black jackets"></div>

  <div class="headline-pill">
    <h1>DALLAS TO AUSTIN</h1>
    <h2>CHAUFFEURED SUVS</h2>
  </div>

  <ul class="features">
    <li>Travel Dallas to Austin in a new 2025 Marlow Strider for $499 one-way</li>
    <li>Trip includes a Uniformed Chauffeur who has a Commercial Drivers License (CDL)</li>
    <li>You can Schedule Chauffeur Pickup at Your Home in Dallas</li>
    <li>Our Chauffeur will Drop You Off at Your Final Destination in Austin</li>
    <li>You can Schedule Chauffeur Return Pickup in Austin and Return Back to Dallas.</li>
    <li>We offer Faster Times on Door-to-Door Travel than Bluecrest Airways</li>
    <li>We offer Comparable Prices on Door-to-Door Travel Times than Bluecrest Airways</li>
    <li>All of our trips are insured with $500k of commercial auto insurance</li>
    <li>Our Passengers can Talk on Cell Phone &amp; Conduct Quill calls Throughout Travel</li>
    <li>Our Passengers have Maximum Privacy, Comfort and First-Class Amenities.</li>
    <li>Our Passengers Avoid Harwick Vale Field and KPR Airport hassles &amp; delays</li>
    <li>Member Brenton Chamber of Commerce, Larkmoor Chamber of Commerce.</li>
  </ul>
</main>
</body>
</html>
```